Website design for an Italian restaurant in Amsterdam

I need a design for a client of mine. It is for Teatro Lunaverde, an Italian restaurant in Amsterdam.
We are going for a clean, modern look but we also need to realise an authentic feel.
The restaurant is located in an old movie theatre, that is where the name Teatro Lunaverde comes from.
Industry/Entity Type
Italian Restaurant
Number of Pages Required
1 page
Font styles to use
Sans Serif
Colors
Designer to choose colors to be used in the design.

```html
<!DOCTYPE html>
<html lang="en">
<head>
<meta charset="utf-8">
<title>Teatro Lunaverde — Italian Restaurant in Amsterdam</title>
<link rel="stylesheet" href="https://fonts.googleapis.com/css2?family=Lora:ital,wght@0,400;0,700;1,400&display=swap">
<style>
:root{
  --accent:#f7931e;
  --ink:#111;
  --muted:#666;
  --paper:#fff;
  --mist:#f1f1f1;
  --night:#0b0b0b;
  --hero-a:#1b2a8a;
  --hero-b:#c7801e;
  --line:#d9d9d9;
}
*{box-sizing:border-box;margin:0;padding:0}
html,body{width:1200px;height:3666px;overflow:hidden;background:var(--paper)}
body{position:relative;font-family:"Lora",serif;color:var(--ink)}
.abs{position:absolute}
.photo{position:absolute;display:block}

/* hero */
.hero{position:absolute;left:0;top:0;width:1200px;height:596px;
  background:radial-gradient(ellipse at 62% 70%,#e3a23a 0%,#9a5a1c 28%,transparent 55%),
  linear-gradient(180deg,#1a2fb8 0%,#132078 45%,#3a2a3a 100%)}
.brand{position:absolute;left:20px;top:16px;color:var(--paper);font-size:44px;line-height:1;font-weight:400}
.brand-sub{position:absolute;left:20px;top:74px;color:var(--paper);font-size:12px;letter-spacing:.5px;text-transform:uppercase}
.nav{position:absolute;left:500px;top:34px;display:flex;gap:0;color:var(--paper);font-size:12px;text-transform:uppercase}
.nav span{padding:0 14px;position:relative}
.nav span+span::before{content:"";position:absolute;left:-2px;top:7px;width:3px;height:3px;border-radius:50%;background:var(--paper)}
.btn-book{position:absolute;left:1027px;top:20px;width:156px;height:41px;border:1px solid var(--paper);color:var(--paper);font-size:12px;display:flex;align-items:center;justify-content:center;gap:16px;text-transform:uppercase}
.hero-kicker{position:absolute;left:120px;top:168px;color:var(--paper);font-size:18px;line-height:22px;text-transform:uppercase}
.hero-title{position:absolute;left:120px;top:222px;color:var(--paper);font-size:47px;line-height:56px;font-weight:700;letter-spacing:1px;text-transform:uppercase}
.btn-learn{position:absolute;left:120px;top:350px;width:120px;height:36px;border-radius:18px;background:var(--accent);color:var(--paper);font-size:11px;display:flex;align-items:center;justify-content:center;text-transform:uppercase}
.hero-call{position:absolute;left:120px;top:428px;color:var(--paper);font-size:18px;line-height:24px;text-transform:uppercase}
.dots{position:absolute;left:588px;top:548px;display:flex;gap:4px}
.dots i{width:8px;height:8px;border-radius:50%;background:var(--paper);display:block}

/* about */
.about{position:absolute;left:0;top:596px;width:1200px;height:670px;background:var(--mist)}
.about-card{position:absolute;left:362px;top:687px;width:476px;height:481px;background:var(--paper)}
.about-title{position:absolute;left:417px;top:722px;color:var(--accent);font-size:29px;line-height:36px}
.tagline{font-style:italic;font-size:17px}
.body-text{font-size:12px;line-height:16px;color:var(--muted)}
.badge{position:absolute;left:419px;top:1060px;width:52px;height:52px;border:2px solid var(--ink);border-radius:10px}
.link-more{position:absolute;font-size:11px;color:var(--muted);text-transform:uppercase;border-bottom:1px solid var(--muted);padding-bottom:3px}

/* booking */
.since{position:absolute;left:120px;top:1420px;font-size:46px}
.book-panel{position:absolute;left:0;top:1266px;width:1200px;height:514px}
.book-title{position:absolute;left:672px;top:1398px;color:var(--paper);font-size:29px}
.field{position:absolute;left:675px;width:256px;height:38px;border-bottom:1px solid #ccc;border-left:1px solid #ccc;color:#aaa;font-size:12px;padding:10px 12px}
.btn-submit{position:absolute;left:675px;top:1652px;width:157px;height:42px;background:var(--paper);color:var(--ink);font-size:12px;display:flex;align-items:center;justify-content:center;gap:14px;text-transform:uppercase}

/* menu */
.section-title{position:absolute;left:0;width:1200px;text-align:center;font-size:44px}
.dish-title{position:absolute;color:var(--accent);font-size:20px}
.dish-text{position:absolute;width:220px;font-size:12px;line-height:15px;color:var(--muted)}
.tag-new{position:absolute;width:64px;height:64px;border-radius:50%;background:var(--paper);font-style:italic;font-size:15px;text-align:center;padding-top:6px}
.btn-menu{position:absolute;left:518px;top:2718px;width:157px;height:41px;border:1px solid var(--ink);font-size:12px;display:flex;align-items:center;justify-content:center;gap:20px;text-transform:uppercase}

/* gallery */
.g-arrow{position:absolute;top:3108px;color:var(--paper);font-size:32px}

/* footer */
.foot-brand{position:absolute;left:117px;top:3410px;font-size:96px;line-height:1}
.foot-col{position:absolute;top:3412px;font-size:12px;line-height:22px}
.foot-col h4{font-size:15px;font-weight:700;margin-bottom:10px}
.social{display:flex;gap:16px;margin-top:6px}
.social i{display:block;width:20px;height:20px;border-radius:50%;background:#555}
.copy{position:absolute;left:0;top:3622px;width:1200px;height:44px;background:var(--night);color:var(--paper);font-size:11px;display:flex;align-items:center;justify-content:center;text-transform:uppercase}
</style>
</head>
<body>

<!-- Hero -->
<section class="hero" role="img" aria-label="Evening street with old Amsterdam canal houses lit in warm light under a deep blue sky"></section>
<div class="brand">TL</div>
<div class="brand-sub">Teatro Lunaverde</div>
<nav class="nav"><span>Home</span><span>About</span><span>Menu</span><span>Blog</span><span>Gallery</span><span>Contacts</span></nav>
<div class="btn-book">Book now <span>›</span></div>
<p class="hero-kicker">Welcome to, Italian<br>restaurant in Amsterdam</p>
<h1 class="hero-title">Teatro<br>Lunaverde</h1>
<div class="btn-learn">Learn more</div>
<p class="hero-call">For reservation call<br>+31 2 0987 6543</p>
<div class="dots"><i></i><i></i><i></i><i></i></div>

<!-- About -->
<section class="about"></section>
<div class="photo" style="left:0;top:687px;width:362px;height:481px;background:linear-gradient(160deg,#2b3340,#6d5a4a 55%,#b6683a)" role="img" aria-label="Pizza chef tossing dough in the kitchen"></div>
<div class="about-card"></div>
<svg class="abs" style="left:340px;top:665px" width="520" height="525" aria-hidden="true">
  <path d="M22 22 L40 4 M22 22 L4 40 M498 22 L480 4 M498 22 L516 40 M22 503 L4 485 M22 503 L40 521 M498 503 L516 485 M498 503 L480 521" stroke="#e8c9a0" stroke-width="1" fill="none"/>
</svg>
<h2 class="about-title">About Teatro<br>Lunaverde<br>Italian restaurant<br>in Amsterdam</h2>
<p class="abs tagline" style="left:417px;top:882px">The Italian restaurant to enjoy life and food.</p>
<p class="abs body-text" style="left:417px;top:922px;width:370px">Nemo enim ipsam voluptatem quia voluptas sit aspernatur aut odit aut fugit, sed quia consequuntur magni dolores eos qui ratione voluptatem sequi nesciunt. Neque porro quisquam est, qui dolorem ipsum quia dolor sit amet, consectetur, adipisci velit, sed quia non numquam eius modi tempora incidunt ut labore et dolore magnam aliquam.</p>
<div class="badge"></div>
<span class="link-more" style="left:488px;top:1075px">Learn more</span>
<div class="photo" style="left:838px;top:687px;width:362px;height:481px;background:linear-gradient(200deg,#dcdcdc,#9a948a 50%,#4a4038)" role="img" aria-label="Chef in white uniform plating food at a steel counter"></div>

<!-- Booking -->
<svg class="book-panel" width="1200" height="514" role="img" aria-label="Dim restaurant interior with warm bokeh lights">
  <defs><radialGradient id="bokeh" cx="0.6" cy="0.4" r="0.7"><stop offset="0" stop-color="#4a3426"/><stop offset="1" stop-color="#0a0807"/></radialGradient></defs>
  <polygon points="655,0 1200,0 1200,514 500,514" fill="url(#bokeh)"/>
</svg>
<h2 class="since">Since 2000</h2>
<p class="abs tagline" style="left:120px;top:1484px">The Italian restaurant to enjoy life and food.</p>
<p class="abs body-text" style="left:120px;top:1524px;width:380px;color:var(--ink)">Nemo enim ipsam voluptatem quia voluptas sit aspernatur aut odit aut fugit, sed quia consequuntur magni dolores eos qui ratione voluptatem sequi nesciunt.</p>
<span class="link-more" style="left:120px;top:1636px;color:var(--ink);border-color:var(--ink)">Learn more</span>
<h2 class="book-title">Book Now</h2>
<div class="field" style="top:1456px">Your Name</div>
<div class="field" style="top:1516px">Email</div>
<div class="field" style="top:1580px">Message</div>
<div class="btn-submit">Book now <span>›</span></div>

<!-- Menu -->
<h2 class="section-title" style="top:1866px">Menu</h2>

<div class="photo" style="left:120px;top:1972px;width:303px;height:230px;background:linear-gradient(135deg,#1c1c1c,#5a3a24 60%,#c06a32)" role="img" aria-label="Pasta with prawns on a dark plate"></div>
<div class="photo" style="left:447px;top:1972px;width:303px;height:230px;background:linear-gradient(135deg,#3a2616,#b8682a 55%,#e0a04a)" role="img" aria-label="Pizza slice with peppers on a board"></div>
<div class="photo" style="left:775px;top:1972px;width:303px;height:230px;background:linear-gradient(135deg,#e9e9e9,#9aa08a 55%,#4a4a3a)" role="img" aria-label="Chef garnishing a plated dish"></div>
<div class="photo" style="left:120px;top:2341px;width:303px;height:230px;background:linear-gradient(135deg,#2a1a12,#7a3e1e 55%,#b9753a)" role="img" aria-label="Glazed roast ribs"></div>
<div class="photo" style="left:447px;top:2341px;width:303px;height:230px;background:linear-gradient(135deg,#1a1a16,#6a6048 55%,#d6cdaa)" role="img" aria-label="Antipasti bowls with dips and vegetables"></div>
<div class="photo" style="left:775px;top:2341px;width:303px;height:230px;background:linear-gradient(135deg,#4a3428,#7a5240 55%,#cfc2b8)" role="img" aria-label="Chocolate dessert with cream"></div>

<div class="tag-new" style="left:349px;top:1944px">New</div>
<div class="tag-new" style="left:670px;top:1944px">New</div>
<div class="tag-new" style="left:983px;top:1944px">New</div>
<div class="tag-new" style="left:349px;top:2313px">New</div>
<div class="tag-new" style="left:670px;top:2313px">New</div>
<div class="tag-new" style="left:983px;top:2313px">New</div>

<h3 class="dish-title" style="left:120px;top:2217px">Lorem Ipsum</h3>
<h3 class="dish-title" style="left:447px;top:2217px">Lorem Ipsum</h3>
<h3 class="dish-title" style="left:775px;top:2217px">Lorem Ipsum</h3>
<p class="dish-text" style="left:120px;top:2250px">Nemo enim ipsam voluptatem quia voluptas</p>
<p class="dish-text" style="left:447px;top:2250px">Nemo enim ipsam voluptatem quia voluptas</p>
<p class="dish-text" style="left:775px;top:2250px">Nemo enim ipsam voluptatem quia voluptas</p>
<h3 class="dish-title" style="left:120px;top:2586px">Lorem Ipsum</h3>
<h3 class="dish-title" style="left:447px;top:2586px">Lorem Ipsum</h3>
<h3 class="dish-title" style="left:775px;top:2586px">Lorem Ipsum</h3>
<p class="dish-text" style="left:120px;top:2619px">Nemo enim ipsam voluptatem quia voluptas</p>
<p class="dish-text" style="left:447px;top:2619px">Nemo enim ipsam voluptatem quia voluptas</p>
<p class="dish-text" style="left:775px;top:2619px">Nemo enim ipsam voluptatem quia voluptas</p>

<div class="btn-menu">Menu <span>›</span></div>

<!-- Gallery -->
<h2 class="section-title" style="top:2842px">Gallery</h2>
<div class="photo" style="left:0;top:2955px;width:381px;height:337px;background:linear-gradient(135deg,#d8d8d8,#8a8478 55%,#4a3a2a)" role="img" aria-label="Chefs working in a busy kitchen"></div>
<div class="photo" style="left:408px;top:2955px;width:384px;height:337px;background:linear-gradient(180deg,#8fb4e0,#b06a3a 55%,#2a3040)" role="img" aria-label="Amsterdam canal houses reflected in the water"></div>
<div class="photo" style="left:816px;top:2955px;width:384px;height:337px;background:linear-gradient(180deg,#5f9fe0,#e8ecef 45%,#6a4a3a)" role="img" aria-label="Sunny rooftop terrace with tables and potted trees"></div>
<span class="g-arrow" style="left:38px">‹</span>
<span class="g-arrow" style="left:1146px">›</span>

<!-- Footer -->
<div class="foot-brand">TL</div>
<div class="foot-col" style="left:379px"><h4>Quick</h4>Home<br>About<br>Menu<br>Gallery<br>Contacts</div>
<div class="foot-col" style="left:530px"><h4>Menu</h4>Pure Veg<br>Pure Non Veg<br>Beverage<br>Itlain Special Food</div>
<div class="foot-col" style="left:718px"><h4>Location</h4>Italian Restaurant<br>12/B, Lindengracht Street<br>Amsterdam, 1015<br><span style="font-size:14px">For reservation call</span><br>+31 2 0987 6543</div>
<div class="foot-col" style="left:938px"><h4>Social Connects</h4><div class="social"><i></i><i></i><i></i><i></i></div></div>
<div class="copy">© Copyright 2018</div>

</body>
</html>
```